Two Versions of a Business Card for a Lawyer

Summary: I need a logo and a business card. The business card is two-sided and comes in two versions. One version is conservative, the other is slightly different with one or more pink embellishments in the logo or somewhere else in the business card.
I'm about to start off as a sole practitioner in criminal and immigration law. I'll largely be working with marginalised communities and in areas of social justice. One of my main focuses will be gendered violence, I'm hoping to specialise my practice towards representing victims of domestic and sexual violence and sex workers. I want a business card which would attract this clientele and make them feel safe to speak with me. I'd also like it to communicate a sense of hope.
However, the business card still has to be very conservative as the legal profession is very stuffy. So I was thinking of having two versions of the same card, one would be very straight forward while the other would have a **pink embellishment** or perhaps several. For example, if the scales of justice were used in the design, maybe the second version would have a pink flower about to bloom on the scale somewhere. Or maybe it's my logo that is different and pink.
While both designs have to be pretty conservative, I still want it to give off a sense that I'm alternative and think outside the box. With lawyers, I think a little bit of deviation goes a long way (less is more).
As far as colour goes (other than the pink embellishment), I was thinking something monochromatic, probably black and white but I am open to considering more colours. I personally love colour, and would love to use more colour, but am hesitant because of the nature of the profession. If you can find a way to use more colour while keeping it conservative and letting the pink pop, I'd be pretty pleased.
In general, I would prefer a clean simplistic design and logo. It should be immediately obvious that I'm a lawyer just by glancing at the card. I'm open to symbols of law, like the scales of justice or lady justice or something else. However, I don't want it to be the same as everyone else's.
Eventually, the design/style should be easy to recreate in the form of a website.
As far as the logo goes, it would probably use a circle as my last name starts with the letter "O". It can be very simple, with just my name and "Barrister & Solicitor". I don't currently have a logo, but the winning designer will be invited to provide a separate file for just the logo for an additional fee (I think it was CA$99). (Please ignore the uploaded logo file, it just wouldn't let me continue without uploading something).
As for the information that should go into the card, I'm still finalizing my address and phone number. So please use a placeholder for now.
Target Market(s)
Women, victims of sexual or domestic violence, refugees, people in need of legal services
Industry/Entity Type
Lawyer
Contact Information for Business Card
Maren Vickery
Barrister & Solicitor
LL.B., B.C.L., B.F.A.
Criminal & Immigration Law
Street address
Toronto, ON
Postal Code
Phone number
Fax number
Email
Logo Text
Maren Vickery, Barrister & Solicitor
Requirements
Must have
- Two versions
- One with pink
- Simplistic
Nice to have
- Maybe more colour
Should not have
- Not too conservative
- Not too predictable

```html
<!DOCTYPE html>
<html lang="en">
<head>
<meta charset="utf-8">
<title>Maren Vickery – Business Card</title>
<link rel="stylesheet" href="https://fonts.googleapis.com/css2?family=Mulish:wght@400;700&display=swap">
<style>
  :root {
    --page-bg: #ece8e4;
    --card-white: #ffffff;
    --ink: #3a3a3a;
    --ink-soft: #555555;
    --pink-light: #f0b3d2;
    --pink-mid: #e77fb7;
    --pink-deep: #d9449a;
    --slate: #4a4a4b;
    --logo-white: #ffffff;
  }
  html, body {
    margin: 0;
    width: 1200px;
    height: 900px;
    overflow: hidden;
    background: var(--page-bg);
    font-family: "Mulish", "Century Gothic", sans-serif;
  }
  .canvas {
    position: relative;
    width: 1200px;
    height: 900px;
  }
  .card {
    position: absolute;
    left: 285px;
    width: 630px;
    height: 360px;
    overflow: hidden;
    box-shadow: 0 8px 24px rgba(0,0,0,0.15);
  }
  .card--front { top: 70px; background: var(--card-white); }
  .card--back { top: 470px; background: var(--slate); }

  .front__panel {
    position: absolute;
    inset: 0;
    width: 630px;
    height: 360px;
  }
  .front__details {
    position: absolute;
    left: 44px;
    top: 56px;
    color: var(--ink);
  }
  .front__name {
    margin: 0;
    font-size: 22px;
    font-weight: 700;
    letter-spacing: 0.3px;
  }
  .front__title, .front__credentials {
    margin: 0;
    font-size: 12.5px;
    line-height: 1.3;
    color: var(--ink-soft);
  }
  .front__practice {
    margin: 26px 0 22px;
    font-size: 22px;
    font-weight: 400;
    letter-spacing: 0.4px;
  }
  .front__contact {
    margin: 0;
    font-style: normal;
    font-size: 14px;
    line-height: 1.4;
    color: var(--ink-soft);
  }

  .brand {
    position: absolute;
    display: flex;
    align-items: center;
    gap: 12px;
    color: var(--logo-white);
    font-family: "Mulish", "Century Gothic", sans-serif;
    font-weight: 400;
    white-space: nowrap;
  }
  .brand__dot {
    border: 3px solid var(--logo-white);
    border-radius: 50%;
    box-sizing: border-box;
  }
  .brand--front { right: 30px; top: 150px; font-size: 22px; }
  .brand--front .brand__dot { width: 44px; height: 44px; }
  .brand--back { left: 50%; top: 50%; transform: translate(-50%, -50%); font-size: 42px; gap: 20px; }
  .brand--back .brand__dot { width: 80px; height: 80px; border-width: 4px; }
</style>
</head>
<body>
<main class="canvas">
  <section class="card card--front" aria-label="Card front">
    <svg class="front__panel" viewBox="0 0 630 360" aria-hidden="true">
      <defs>
        <linearGradient id="pinkPanel" x1="0" y1="0" x2="1" y2="0">
          <stop offset="0" stop-color="var(--pink-deep)"/>
          <stop offset="0.35" stop-color="var(--pink-mid)"/>
          <stop offset="0.6" stop-color="var(--pink-light)"/>
          <stop offset="1" stop-color="var(--pink-deep)"/>
        </linearGradient>
      </defs>
      <polygon points="420,0 630,0 630,360 330,360" fill="url(#pinkPanel)"/>
    </svg>
    <div class="front__details">
      <h1 class="front__name">Maren Vickery</h1>
      <p class="front__title">Barrister &amp; Solicitor</p>
      <p class="front__credentials">LL.B., B.C.L., B.F.A.</p>
      <h2 class="front__practice">Criminal &amp; Immigration Law</h2>
      <address class="front__contact">
        123 Cryout Bldg., Anywhere St.<br>
        Toronto, ON 11001100<br>
        000-000-0000<br>
        000-000-0000<br>
        Name@company.com
      </address>
    </div>
    <div class="brand brand--front">
      <span class="brand__dot" aria-hidden="true"></span>
      <span class="brand__name">Maren Vickery</span>
    </div>
  </section>

  <section class="card card--back" aria-label="Card back">
    <div class="brand brand--back">
      <span class="brand__dot" aria-hidden="true"></span>
      <span class="brand__name">Maren Vickery</span>
    </div>
  </section>
</main>
</body>
</html>
```